catering postcard

We need a postcard that lets offices know that we cater and can deliver our delicious food to their office/meeting/event.

We are a mom and pop, super busy, well-loved Italian restaurant.
(check us out at pennysbistrokitchen.com)

The final design should communicate delicious food, brought to your place of work. It arrives on time and is hot and ready to be devoured.

We'd like to see bright colors and a huge impact on our lunch time catering sales.

Catering

```html
<!DOCTYPE html>
<html lang="en">
<head>
<meta charset="utf-8">
<title>Penny's Bistro – Catering Postcard</title>
<link rel="stylesheet" href="https://fonts.googleapis.com/css2?family=Arvo:wght@400;700&family=Roboto+Condensed:wght@400;700&display=swap">
<style>
  :root {
    --stage: #c3121b;
    --paper: #ffffff;
    --basil: #3a8a2e;
    --basil-dark: #2f6e22;
    --brand-red: #8e1414;
    --band-red: #b5121b;
    --band-dark: #7d0a0f;
    --gold: #ffd21f;
    --sauce: #c23a1f;
    --sauce-dark: #6e1a10;
    --cheese: #efe9dc;
    --plate: #f4f1ea;
    --table: #3a2518;
    --cake: #c98e4c;
    --cake-dark: #9c6532;
    --frosting: #f5f1e8;
    --cream-bg: #e8dcc2;
    --soup: #e0542a;
  }
  * { margin: 0; padding: 0; box-sizing: border-box; }
  html, body { width: 1200px; height: 841px; overflow: hidden; }
  body { position: relative; background: var(--stage); font-family: "Arvo", serif; }

  .card { position: absolute; background: var(--paper); overflow: hidden; }
  .card--back { left: 33px; top: 36px; width: 716px; height: 551px; }
  .card--front { left: 435px; top: 245px; width: 716px; height: 552px; }

  .photo { position: absolute; }
  .photo--meatballs {
    background:
      radial-gradient(ellipse 34% 16% at 40% 78%, rgba(60,130,40,.95) 0%, rgba(60,130,40,.7) 55%, rgba(60,130,40,0) 100%),
      radial-gradient(ellipse 42% 22% at 45% 18%, rgba(239,233,220,.95) 0%, rgba(239,233,220,.55) 60%, rgba(239,233,220,0) 100%),
      radial-gradient(ellipse 30% 22% at 85% 55%, rgba(239,233,220,.8) 0%, rgba(239,233,220,0) 100%),
      radial-gradient(ellipse 25% 22% at 10% 60%, rgba(239,233,220,.75) 0%, rgba(239,233,220,0) 100%),
      radial-gradient(ellipse 62% 55% at 50% 48%, var(--sauce) 0%, #a8301a 55%, rgba(168,48,26,0) 100%),
      linear-gradient(180deg, var(--table) 0%, #5a3a28 25%, var(--plate) 70%, #d9d3c8 100%);
  }
  .photo--cake {
    background:
      radial-gradient(ellipse 45% 35% at 40% 50%, var(--cake) 0%, var(--cake-dark) 70%, rgba(156,101,50,0) 100%),
      radial-gradient(ellipse 40% 45% at 72% 60%, var(--frosting) 0%, rgba(245,241,232,.9) 60%, rgba(245,241,232,0) 100%),
      linear-gradient(180deg, var(--cream-bg) 0%, #d9c9a6 45%, var(--plate) 78%, #e6b04a 88%, var(--plate) 100%);
  }
  .photo--soup {
    background:
      radial-gradient(ellipse 44% 80% at 52% 55%, var(--soup) 0%, #cf4623 70%, rgba(207,70,35,0) 100%),
      linear-gradient(180deg, #ece6db 0%, var(--plate) 100%);
  }

  /* back card */
  .back-photo { left: 0; top: 194px; width: 357px; height: 275px; }
  .back-header { position: absolute; left: 0; top: 0; width: 357px; height: 225px; }
  .back-header svg { position: absolute; inset: 0; }
  .brand-name { font-family: "Arvo", serif; font-weight: 700; letter-spacing: 1px; }
  .back-header .brand-name {
    position: absolute; left: 0; width: 357px; top: 62px; text-align: center;
    color: var(--paper); font-size: 42px;
  }
  .address {
    position: absolute; left: 0; width: 357px; top: 167px; text-align: center;
    font-family: "Roboto Condensed", sans-serif; color: var(--paper); font-size: 16px;
  }

  /* front card */
  .front-logo { position: absolute; left: 0; top: 0; width: 358px; height: 200px; display: flex; align-items: center; justify-content: center; }
  .front-logo .brand-name { color: var(--brand-red); font-size: 44px; }
  .phone-band {
    position: absolute; left: 0; top: 200px; width: 358px; height: 46px;
    background: linear-gradient(90deg, var(--band-dark), var(--band-red) 40%, var(--band-red) 60%, var(--band-dark));
    display: flex; align-items: center; padding-left: 55px; gap: 10px;
    font-family: "Roboto Condensed", sans-serif; font-weight: 700; font-size: 29px; color: var(--gold);
  }
  .phone-band svg { width: 26px; height: 26px; }
  .front-cake { left: 0; top: 275px; width: 358px; height: 277px; }
  .front-meatballs { left: 358px; top: 0; width: 358px; height: 275px; }
  .promise {
    position: absolute; left: 358px; top: 275px; width: 358px; height: 177px;
    background: radial-gradient(ellipse at 50% 50%, var(--band-red) 0%, var(--band-dark) 100%);
    display: flex; align-items: center; justify-content: center; text-align: center;
    color: var(--gold); font-size: 22px; line-height: 37px; font-weight: 700;
  }
  .front-soup { left: 358px; top: 452px; width: 358px; height: 100px; }
</style>
</head>
<body>
  <section class="card card--back">
    <div class="photo photo--meatballs back-photo" role="img" aria-label="Photo of meatballs in tomato sauce topped with grated parmesan and a basil leaf"></div>
    <header class="back-header">
      <svg width="357" height="225" viewBox="0 0 357 225" aria-hidden="true">
        <path d="M0 0 H357 V190 Q180 250 0 190 Z" fill="var(--basil)"/>
      </svg>
      <div class="brand-name">Penny's Bistro</div>
      <p class="address">48 Maple Grove Lane, Fairhaven, Alabama 35010</p>
    </header>
  </section>

  <section class="card card--front">
    <div class="front-logo"><span class="brand-name">Penny's Bistro</span></div>
    <div class="phone-band">
      <svg viewBox="0 0 26 26" aria-hidden="true">
        <circle cx="13" cy="13" r="12" fill="var(--gold)"/>
        <path d="M10 7 L12 10 L10.5 12 Q12 15 14 15.5 L16 14 L19 16 L17.5 19 Q11 19 7.5 11 Z" fill="var(--band-red)"/>
      </svg>
      <span>(205) 555-0142</span>
    </div>
    <div class="photo photo--cake front-cake" role="img" aria-label="Photo of a slice of layered carrot cake with cream cheese frosting on a plate"></div>
    <div class="photo photo--meatballs front-meatballs" role="img" aria-label="Photo of meatballs in tomato sauce topped with grated parmesan and a basil leaf"></div>
    <p class="promise">Delicious Food at<br>Your Workplace<br>On Time and is Hot and<br>Ready to be Devoured.</p>
    <div class="photo photo--soup front-soup" role="img" aria-label="Photo of a bowl of tomato soup garnished with basil and herbs"></div>
  </section>
</body>
</html>
```